Card design for Heating and Cooling company

this is for a heating and cooling company we recently updated our logo and need to update our cards. We attached our logo so you can incorporate it into the card. We specialize in residential and commercial furnace and air condition repairs. Have been in business since 2014.

Phone number 618.274.9031

We need the following phrases
:Repairs, Installations, and maintenance
:Quality work at reasonable prices
:residential/commercial
:Licensed &Insured
:Email Pinecresthvac47@mailbox-demo.com
Name: Tadeusz K (Ted)
Also on back side I would like my logo with wording :Thank you for your business and refferal

Industry/Entity Type

Hvac

Contact Information for Business Card

:residential/commercial
:Licensed & Insured
Name: Tadeusz K (Ted)
Number:618.274.9030

Requirements
Must have
• Blue and red colors
Nice to have
• Maybe a pic of a furnace or air conditioner

```html
<!DOCTYPE html>
<html lang="en">
<head>
<meta charset="utf-8">
<title>Pinecrest Heating &amp; Cooling – Business Card</title>
<link rel="stylesheet" href="https://fonts.googleapis.com/css2?family=PT+Sans:ital,wght@0,400;0,700;1,700&family=PT+Sans+Narrow:wght@400&display=swap">
<style>
  :root {
    --page-bg: #ececec;
    --blue-light: #3aa6ee;
    --blue-mid: #1677d2;
    --blue-deep: #0b4c9c;
    --red: #dc1b1b;
    --red-light: #ee2a24;
    --text-light: #f2f7fc;
    --text-soft: #dbe9f7;
    --thanks: #f1c9c2;
  }
  html, body {
    margin: 0;
    padding: 0;
    width: 1200px;
    height: 1120px;
    overflow: hidden;
    background: var(--page-bg);
  }
  .business-card {
    position: absolute;
    left: 75px;
    top: 260px;
    width: 1050px;
    height: 600px;
    overflow: hidden;
    background:
      radial-gradient(ellipse 60% 55% at 18% 15%, rgba(255,255,255,0.28), rgba(255,255,255,0) 70%),
      linear-gradient(90deg, var(--blue-light) 0%, var(--blue-mid) 45%, var(--blue-deep) 68.5%, var(--red) 69%, var(--red-light) 100%);
    box-shadow: 0 10px 30px rgba(0,0,0,0.18);
    font-family: "PT Sans", Arial, sans-serif;
    color: var(--text-light);
  }
  .owner-name {
    position: absolute;
    left: 37px;
    top: 64px;
    margin: 0;
    font-size: 33px;
    font-weight: 700;
    letter-spacing: 0.3px;
  }
  .contact-list {
    position: absolute;
    left: 37px;
    top: 246px;
    margin: 0;
    padding: 0;
    list-style: none;
    font-size: 26px;
    line-height: 34px;
  }
  .contact-list li { display: flex; align-items: center; gap: 12px; }
  .contact-icon { width: 22px; height: 22px; fill: var(--text-light); flex: none; }
  .service-list {
    position: absolute;
    left: 37px;
    top: 382px;
    margin: 0;
    padding: 0 0 0 30px;
    font-family: "PT Sans Narrow", Arial, sans-serif;
    font-size: 25px;
    line-height: 34px;
    color: var(--text-soft);
  }
  .thanks-line {
    position: absolute;
    left: 37px;
    top: 524px;
    margin: 0;
    font-size: 26px;
    font-weight: 700;
    font-style: italic;
    color: var(--thanks);
  }
  .brand {
    position: absolute;
    left: 590px;
    top: 255px;
    display: flex;
    align-items: center;
    gap: 16px;
  }
  .brand-dot {
    width: 46px;
    height: 46px;
    border-radius: 50%;
    background: var(--text-light);
    flex: none;
  }
  .brand-name {
    margin: 0;
    font-size: 40px;
    font-weight: 700;
    line-height: 1.05;
    color: var(--text-light);
  }
</style>
</head>
<body>
  <section class="business-card">
    <h1 class="owner-name">Tadeusz K (Ted)</h1>

    <ul class="contact-list">
      <li>
        <svg class="contact-icon" viewBox="0 0 24 24" aria-hidden="true"><path d="M6.6 10.8a15.1 15.1 0 0 0 6.6 6.6l2.2-2.2a1 1 0 0 1 1-.25 11.4 11.4 0 0 0 3.6.57 1 1 0 0 1 1 1V20a1 1 0 0 1-1 1A17 17 0 0 1 3 4a1 1 0 0 1 1-1h3.5a1 1 0 0 1 1 1c0 1.25.2 2.45.57 3.57a1 1 0 0 1-.25 1z"/></svg>
        618.274.9030
      </li>
      <li>
        <svg class="contact-icon" viewBox="0 0 24 24" aria-hidden="true"><path d="M2 5h20v14H2z" opacity="0.9"/><path d="M2 5l10 8 10-8" fill="none" stroke="#1a6fc8" stroke-width="2"/></svg>
        Pinecresthvac47@mailbox-demo.com
      </li>
      <li>
        <svg class="contact-icon" viewBox="0 0 24 24" aria-hidden="true"><circle cx="12" cy="12" r="10"/><path d="M2 12h20M12 2c3 3 3 17 0 20M12 2c-3 3-3 17 0 20" fill="none" stroke="#1a6fc8" stroke-width="1.6"/></svg>
        www.pinecrest-demo.com
      </li>
    </ul>

    <ul class="service-list">
      <li>Repairs, Installations, &amp; maintenance</li>
      <li>Quality work at reasonable prices</li>
      <li>residential/commercial</li>
      <li>Licensed &amp; Insured</li>
    </ul>

    <p class="thanks-line">Thank you for your business &amp; refferal</p>

    <div class="brand">
      <span class="brand-dot"></span>
      <p class="brand-name">Pinecrest<br>Heating &amp; Cooling</p>
    </div>
  </section>
</body>
</html>
```